Business Card Design

Marlow Signworks and 7Q window film

Reason: I need more and different designs with "7Q" red logo I will upload image

Industry/Entity Type

Business

Contact Information for Business Card

I have business logo I just want a new updated card design.

Requirements
Must have
• Original 7Q Red logo

```html
<!DOCTYPE html>
<html lang="en">
<head>
<meta charset="utf-8">
<title>Prairie Solar Control &amp; Marlow Signworks – Business Card</title>
<link rel="stylesheet" href="https://fonts.googleapis.com/css2?family=Open+Sans:wght@400;600;700&display=swap">
<style>
  :root {
    --bg: #9a9a9a;
    --card: #ffffff;
    --ink: #111111;
    --green: #2e7d32;
    --green-dark: #1f5a24;
    --muted: #333333;
    --mark: #d9d9d9;
  }
  * { box-sizing: border-box; margin: 0; padding: 0; }
  html, body { width: 1200px; height: 894px; overflow: hidden; }
  body {
    background: var(--bg);
    font-family: "Open Sans", Arial, sans-serif;
    position: relative;
  }
  .card {
    position: absolute;
    top: 287px;
    width: 560px;
    height: 320px;
    background: var(--card);
    overflow: hidden;
  }
  .card--front { left: 27px; border-bottom: 3px solid var(--green-dark); }
  .card--back { left: 613px; }

  .edge-tab { position: absolute; background: var(--ink); }
  .card--front .edge-tab { left: 0; top: 86px; width: 34px; height: 46px; }
  .card--back .edge-tab { right: 0; top: 160px; width: 26px; height: 48px; }

  .brand {
    position: absolute;
    display: flex; align-items: flex-start; gap: 12px;
  }
  .brand__mark {
    width: 30px; height: 30px; flex: none; margin-top: 3px;
    background: var(--mark);
  }
  .brand__text {
    font-weight: 700; color: var(--green);
    text-transform: uppercase; line-height: 1.1;
  }
  .brand__name { display: block; font-size: 30px; letter-spacing: 0.5px; }
  .brand__tagline { display: block; font-size: 16px; letter-spacing: 0.3px; }
  .card--front .brand { left: 56px; top: 28px; }
  .card--back .brand { left: 180px; top: 62px; }

  .person { position: absolute; left: 56px; top: 150px; }
  .person__name {
    font-weight: 700; font-size: 23px; color: var(--green);
    letter-spacing: 1px; text-transform: uppercase;
  }
  .person__role {
    font-size: 12px; color: var(--ink);
    letter-spacing: 6px; text-transform: uppercase;
  }

  .contact {
    position: absolute; left: 330px; top: 192px;
    list-style: none; font-size: 12.5px; font-weight: 600; color: var(--ink);
  }
  .contact li { display: flex; gap: 10px; align-items: flex-start; margin-bottom: 7px; line-height: 1.2; }
  .contact svg { width: 15px; height: 15px; flex: none; fill: var(--green); }

  .social {
    position: absolute; left: 40px; right: 40px; bottom: 38px;
    display: flex; justify-content: space-between; list-style: none;
    font-size: 13px; color: var(--muted);
  }
  .social li { display: flex; align-items: center; gap: 8px; }
  .social__mark { width: 18px; height: 18px; background: var(--green); border-radius: 2px; }
</style>
</head>
<body>
  <section class="card card--front" aria-label="Business card front">
    <span class="edge-tab"></span>
    <div class="brand">
      <span class="brand__mark"></span>
      <p class="brand__text">
        <span class="brand__name">Prairie</span>
        <span class="brand__tagline">Solar Control &amp;<br>Marlow Signworks</span>
      </p>
    </div>
    <div class="person">
      <p class="person__name">Daniel Reyes</p>
      <p class="person__role">General Manager</p>
    </div>
    <ul class="contact">
      <li>
        <svg viewBox="0 0 16 16"><path d="M8 1 1 7.5h2V15h4v-4h2v4h4V7.5h2z"/></svg>
        <span>41 Harbor Street,<br>Suite 6</span>
      </li>
      <li>
        <svg viewBox="0 0 16 16"><path d="M8 1a7 7 0 1 0 0 14A7 7 0 0 0 8 1zm0 1.5c.8 0 1.7 1.5 2 3.7H6c.3-2.2 1.2-3.7 2-3.7zM2.6 7.2h2.3v1.6H2.6zm8.5 0h2.3v1.6h-2.3zM6 7.2h4v1.6H6zm0 2.6h4c-.3 2.2-1.2 3.7-2 3.7s-1.7-1.5-2-3.7z"/></svg>
        <span>www.yourwebsite.com</span>
      </li>
      <li>
        <svg viewBox="0 0 16 16"><path d="M1 3h14v10H1zm1.5 1.5v.3L8 9l5.5-4.2v-.3z"/></svg>
        <span>yourname@email.com</span>
      </li>
      <li>
        <svg viewBox="0 0 16 16"><path d="M4 1.5 6.2 4 5 6c.9 2 2.6 3.8 5 5l2-1.2 2.5 2.2-1.5 2.5C7 14 2 9 1.5 3z"/></svg>
        <span>012 345 6789</span>
      </li>
    </ul>
  </section>

  <section class="card card--back" aria-label="Business card back">
    <span class="edge-tab"></span>
    <div class="brand">
      <span class="brand__mark"></span>
      <p class="brand__text">
        <span class="brand__name">Prairie</span>
        <span class="brand__tagline">Solar Control &amp;<br>Marlow Signworks</span>
      </p>
    </div>
    <ul class="social">
      <li><span class="social__mark"></span><span>yourname</span></li>
      <li><span class="social__mark"></span><span>@yourname</span></li>
      <li><span class="social__mark"></span><span>yourname</span></li>
    </ul>
  </section>
</body>
</html>
```